Business Card Design Project

I have attached the logo and the colour pallete for the branding for the company.

Creative designs for business cards are needed.

The Company is modern corporate.

Industry/Entity Type

Business

```html
<!DOCTYPE html>
<html lang="en">
<head>
<meta charset="utf-8">
<title>Business Card – Front</title>
<link rel="stylesheet" href="https://fonts.googleapis.com/css2?family=Quicksand:wght@500;600&display=swap">
<style>
  :root {
    --plum-light: #a887a8;
    --plum-mid: #6e446c;
    --plum-dark: #461646;
    --rust: #a65e2e;
    --orange: #e88136;
    --crimson: #d62340;
    --steel: #7d7f83;
    --white: #ffffff;
  }
  html, body {
    margin: 0;
    padding: 0;
    width: 1200px;
    height: 718px;
    overflow: hidden;
    background: #ffffff;
  }
  .card {
    position: relative;
    width: 1200px;
    height: 718px;
    overflow: hidden;
    background: radial-gradient(circle at 0 0, var(--plum-light) 0%, var(--plum-mid) 45%, var(--plum-dark) 100%);
    font-family: "Quicksand", sans-serif;
    color: var(--white);
  }
  .card-shapes {
    position: absolute;
    inset: 0;
    width: 1200px;
    height: 718px;
  }
  .headline {
    position: absolute;
    left: 40px;
    margin: 0;
    font-weight: 500;
    font-size: 80px;
    line-height: 1;
    letter-spacing: 1px;
  }
  .headline--your { top: 110px; }
  .headline--info { top: 222px; }
  .brand-name {
    position: absolute;
    right: 64px;
    top: 52px;
    margin: 0;
    font-size: 68px;
    font-weight: 600;
    line-height: 1;
    letter-spacing: -1px;
  }
  .contact-line {
    position: absolute;
    left: 270px;
    top: 669px;
    margin: 0;
    font-size: 34px;
    font-weight: 600;
    line-height: 1;
  }
</style>
</head>
<body>
  <div class="card">
    <svg class="card-shapes" viewBox="0 0 1120 670" preserveAspectRatio="none" aria-hidden="true">
      <!-- title pill -->
      <path d="M0 72 H450 A150.5 150.5 0 0 1 450 373 H0 Z" fill="var(--rust)"/>
      <!-- contact band -->
      <path d="M140 616 H646 Q654 616 654 624 V670 H140 Z" fill="var(--crimson)"/>
      <!-- corner frame -->
      <path d="M1120 505 V528 L978 670 H952 Z" fill="var(--steel)"/>
      <path d="M654 662 H962 L954 670 H654 Z" fill="var(--steel)"/>
      <!-- orange ring and disc -->
      <path d="M0 428 A242 242 0 0 1 242 670 H204 A204 204 0 0 0 0 466 Z" fill="var(--orange)"/>
      <path d="M0 515 A155 155 0 0 1 155 670 H0 Z" fill="var(--orange)"/>
    </svg>

    <p class="headline headline--your">Your</p>
    <p class="headline headline--info">Info</p>

    <p class="brand-name">novaroute</p>

    <p class="contact-line">Website / Email / Name</p>
  </div>
</body>
</html>
```